Tarrow Cat Hotel needs a website and a logo :)

I need a web design for my pet hotel. I will use it in Wordpress, probable with Elementor, so if you can also offer the WP template creation, that's a bonus but I don't wanna book the coded-website option here as I don't think that applies to WP. It would be great if you come up with a logo as well.

Here some info:

Modern, premium cat boarding with a vet on-site

Tarrow Cat Hotel is a boutique cat boarding facility in Kaiwaro, New Zealand, offering high-quality, vet-supervised care for all cats, including those with special medical needs. Unlike standard catteries, we focus on low-stress boarding, with separate spaces for special-needs and healthy cats, ensuring a safe, comfortable, and peaceful environment. We also prioritize convenience with self check-in and check-out, leveraging technology to enhance the experience.

Target Market(s)

Cat owners for short term to long term stays that don't want the cheapest option and will value that we have a vet on-site

Industry/Entity Type

cat boarding

Number of Pages Required

5+ page

Font styles to use
Sans Serif
Other font styles liked:
• Nothing that needs installation or a license. Please use Google Fonts.

Requirements
Must have
• Landing page, about us, services, blog and contact page - the landing page should have the typical sales layout with hero image top right, a tag line "Modern, premium cat boarding with a vet on-site" and 2 paragraphs. Paragraph 1 (Problem): Leaving your cat behind can be stressful, especially if they need special care. Standard catteries often lack vet oversight and a calm, tailored environment. Paragraph 2 (Solution): At Tarrow Cat Hotel, we offer premium, vet-supervised boarding with separate spaces for special-needs and healthy cats. Our self check-in and tech-driven system makes drop-offs and pick-ups effortless... you know the drill :)
Nice to have
• Ask ChatGPT for some ideas and give it the business plan: https://files.brimlodge.example/doc/8qTxR2vLmPz4KwYc7NbHs3JfDgUeVa1oZiQy/view?share=open
Should not have
• NO DOGS :)

```html
<!DOCTYPE html>
<html lang="en">
<head>
<meta charset="utf-8">
<title>Tarrow Cat Hotel</title>
<link href="https://fonts.googleapis.com/css2?family=Poppins:wght@400;500;600;700;800&display=swap" rel="stylesheet">
<style>
:root{
  --orange:#f7821f;
  --pink:#f23fa2;
  --purple:#8a52d6;
  --yellow:#fdd944;
  --ink:#111111;
  --text:#2b2b2b;
  --muted:#8d8d8d;
  --cream:#faf7f2;
  --field:#f3f3f3;
  --black:#121212;
}
*{box-sizing:border-box;margin:0;padding:0}
html,body{width:1200px;height:4062px;overflow:hidden}
body{font-family:'Poppins',sans-serif;color:var(--text);background:#fff;position:relative}
.abs{position:absolute}
.topbar{left:0;top:0;width:1200px;height:35px;background:var(--black);color:#fff;font-size:12px}
.topbar .info{position:absolute;left:165px;top:9px;display:flex;gap:16px;align-items:center}
.topbar .info span{display:flex;align-items:center;gap:6px}
.topbar .socials{position:absolute;right:166px;top:12px;display:flex;gap:7px}
.topbar .socials i{width:11px;height:11px;border-radius:50%;background:var(--orange);display:block}
.header{left:0;top:35px;width:1200px;height:80px;background:#fff}
.brand{position:absolute;left:178px;top:22px;display:flex;align-items:center;gap:12px}
.brand .mark{width:38px;height:38px;background:var(--orange);border-radius:6px}
.brand .name{font-size:25px;font-weight:500;color:var(--orange);letter-spacing:1px}
.nav{position:absolute;left:670px;top:28px;display:flex;align-items:center;gap:30px;font-size:12.5px;font-weight:600;color:var(--ink)}
.btn{display:inline-block;background:var(--orange);color:#fff;font-weight:600;border-radius:3px;text-align:center;box-shadow:0 3px 0 rgba(0,0,0,.12)}
.nav .btn{padding:6px 18px;font-size:12.5px}
.hero{left:0;top:115px;width:1200px;height:760px;overflow:hidden}
.hero-photo{position:absolute;left:150px;top:0;width:1050px;height:760px;background:linear-gradient(90deg,#fff 0%,rgba(255,255,255,.6) 25%,rgba(238,180,120,.55) 50%,#e9b184 70%,#d8cbc5 100%)}
.hero-wave{position:absolute;left:0;bottom:0}
.hero h1{position:absolute;left:166px;top:178px;font-size:46px;line-height:54px;font-weight:700;color:#2a2a2a;letter-spacing:-1px}
.note{position:absolute;background:rgba(255,255,255,.78);border-radius:18px;font-size:13px;line-height:20px;color:#222}
.note .tag{position:absolute;font-weight:700;font-size:14px;letter-spacing:1px;transform:rotate(-90deg);transform-origin:left top}
.label{font-size:22px;font-weight:700;color:var(--orange);display:flex;align-items:center;gap:8px}
.label i{width:12px;height:12px;border-radius:50%;background:var(--orange);display:block}
.h2{font-size:35px;line-height:39px;font-weight:700;color:var(--ink)}
.about-copy{left:181px;top:1140px;width:398px}
.about-copy p{font-size:11.6px;line-height:19.5px;text-align:justify;color:#222;margin-bottom:19px}
.photo-circle{position:absolute;border-radius:50%}
.services{left:0;top:1569px;width:1200px;height:894px;background:var(--cream)}
.center{text-align:center;width:1200px;left:0}
.sub{font-size:12.3px;line-height:19px;color:#222}
.card-img{position:absolute}
.panel{position:absolute;color:#fff;text-align:center;padding:22px 30px}
.panel h3{font-size:22px;line-height:27px;font-weight:700;padding-bottom:12px;border-bottom:1px solid rgba(255,255,255,.6);margin-bottom:12px}
.panel p{font-size:12.3px;line-height:19px;margin-bottom:18px}
.post{position:absolute;width:418px}
.post .img{height:302px;border-radius:0 0 30px 30px}
.post .meta{margin:40px 30px 0;font-size:13px;color:#111}
.post .meta b{font-weight:500;color:var(--orange)}
.post h4{margin:14px 30px 0;font-size:19px;line-height:28px;font-weight:600;color:#111}
.post p{margin:14px 20px 0 30px;font-size:12.6px;line-height:21.5px;color:var(--muted)}
.post .more{margin:16px 30px 0;font-size:14px;font-weight:600;color:#111}
.field{position:absolute;left:664px;width:353px;background:var(--field);border-radius:3px;font-size:10px;color:#aaa;padding:12px 8px}
.footer{left:0;top:3991px;width:1200px;height:71px;background:var(--black);color:#fff;font-size:14px;text-align:center;line-height:71px}
</style>
</head>
<body>

<div class="abs topbar">
  <div class="info">
    <span><svg width="10" height="13" viewBox="0 0 10 13"><path d="M5 0a5 5 0 0 0-5 5c0 3.5 5 8 5 8s5-4.5 5-8a5 5 0 0 0-5-5zm0 7a2 2 0 1 1 0-4 2 2 0 0 1 0 4z" fill="#f7821f"/></svg>48 Harrowfield Lane, Stoke, NZ, 07011</span>
    <span><svg width="13" height="10" viewBox="0 0 13 10"><rect width="13" height="10" rx="1" fill="#f7821f"/><path d="M0 1l6.5 5L13 1" stroke="#121212" fill="none"/></svg>info@tarrowcathotel.com</span>
  </div>
  <div class="socials"><i></i><i></i><i></i></div>
</div>

<header class="abs header">
  <div class="brand"><span class="mark"></span><span class="name">Tarrow Cat Hotel</span></div>
  <nav class="nav"><span>Home</span><span>About us</span><span>Services</span><span>Blog</span><span class="btn">Contact</span></nav>
</header>

<section class="abs hero">
  <div class="hero-photo" role="img" aria-label="Woman kissing an orange tabby cat held close to her cheek"></div>
  <svg class="hero-wave" width="1200" height="120" viewBox="0 0 1200 120"><path d="M0 0 C250 120 500 120 800 60 C950 30 1100 10 1200 60 L1200 120 L0 120Z" fill="#fff"/></svg>
  <h1>Modern, Premium<br>Cat Boarding with<br>a vet on-site</h1>
  <div class="note" style="left:173px;top:355px;width:344px;height:130px;padding:27px 12px 0 45px">
    <span class="tag" style="left:14px;top:105px;color:var(--pink)">PROBLEM</span>
    Leaving your cat behind can be stressful, especially if they need special care. Standard catteries often lack vet oversight and a calm, tailored environment.
  </div>
  <div class="note" style="left:214px;top:500px;width:401px;height:147px;padding:22px 12px 0 54px">
    <span class="tag" style="left:18px;top:112px;color:var(--purple)">SOLUTION</span>
    At Tarrow Cat Hotel, we offer premium, vet-supervised boarding with separate spaces for special-needs and healthy cats. Our self check-in and tech-driven system makes drop-offs and pick-ups effortless... you know the drill :)
  </div>
</section>

<section class="about">
  <div class="abs label" style="left:181px;top:1012px">About us <i></i></div>
  <h2 class="abs h2" style="left:181px;top:1045px">Premium Cat<br>Retreat with Vet On-Site</h2>
  <div class="abs about-copy">
    <p>Tarrow Cat Hotel is a boutique boarding facility in Kaiwaro, New Zealand, designed to give cats a safe, comfortable, and stress-free stay. The maximum capacity will be 25 cats. Run by a trusted veterinarian, we offer personalised care for all cats, from those needing a cozy place to stay while their owners are away to those requiring extra attention due to age, illness, or special needs.</p>
    <p>Standard boarding cats enjoy their own dedicated spaces, separate from those needing special care, so every feline guest can relax in peace. Cats can also be housed together in the same cage if they are from the same household. With a strong focus on well-being, comfort, and expert supervision, we're here to make every stay feel like home. We also prioritize convenience with self check-in and check-out, leveraging technology to enhance the experience.</p>
  </div>
  <span class="abs btn" style="left:183px;top:1454px;width:131px;height:36px;line-height:36px;font-size:14px">Read more</span>
  <div class="photo-circle" style="left:629px;top:875px;width:536px;height:536px;border:6px solid var(--purple);background:linear-gradient(135deg,#dfe4ea,#e8c7a8 55%,#c99a6c)" role="img" aria-label="Woman nose to nose with an orange tabby cat standing on a shelf"></div>
  <div class="photo-circle" style="left:606px;top:1131px;width:324px;height:324px;border:6px solid var(--pink);background:linear-gradient(135deg,#f2f2f2,#d9c2a6 55%,#3b3b3b)" role="img" aria-label="Curious cat peeking out from behind a white door"></div>
</section>

<section class="abs services">
  <div class="abs label center" style="top:41px;justify-content:center">Our Services <i></i></div>
  <h2 class="abs h2 center" style="top:78px">Community Engagement<br>&amp; Social Responsibility</h2>
  <p class="abs sub center" style="top:176px">Tarrow Cat Hotel will integrate modern technology to enhance convenience and<br>provide peace of mind for pet owners.</p>

  <div class="card-img" style="left:147px;top:308px;width:291px;height:228px;border-radius:145px 145px 0 0;background:linear-gradient(160deg,#e8e3dc,#c8a27a 60%,#8fb8d6)" role="img" aria-label="Ginger cat sitting beside a scratching post"></div>
  <div class="panel" style="left:147px;top:544px;width:291px;height:227px;background:var(--pink);border-radius:0 0 145px 145px">
    <h3>Accommodation<br>Options</h3>
    <p>4 Large Suites – Spacious and designed for ultimate comfort.</p>
    <p>8 Small Suites – Half-height enclosures for a cozy retreat.</p>
  </div>

  <div class="panel" style="left:454px;top:257px;width:290px;height:224px;background:var(--yellow);border-radius:145px 145px 0 0;padding-top:44px">
    <h3>Suite Features</h3>
    <p>A cat tree with scratch rope for climbing and scratching.</p>
    <p>A comfortable chair with a cushion for lounging.</p>
  </div>
  <div class="card-img" style="left:454px;top:494px;width:290px;height:227px;border-radius:0 0 145px 145px;background:linear-gradient(160deg,#3a3a3a,#cfc8bd 55%,#f0ece6)" role="img" aria-label="White fluffy cat on a cat tree platform"></div>

  <div class="card-img" style="left:765px;top:304px;width:291px;height:227px;border-radius:145px 145px 0 0;background:linear-gradient(160deg,#5b6068,#9fa4a8 50%,#c2783e)" role="img" aria-label="Grey tabby cat peering out from a shelf"></div>
  <div class="panel" style="left:765px;top:544px;width:291px;height:227px;background:var(--purple);border-radius:0 0 145px 145px;padding:22px 20px">
    <h3>Special Facilities</h3>
    <p>1 Office – Located at the front for administration and customer service.</p>
    <p>1 Storage Room – Positioned at the back for supplies and cleaning equipment.</p>
  </div>

  <span class="abs btn" style="left:535px;top:771px;width:200px;height:41px;line-height:41px;font-size:14px">View more services</span>
</section>

<section class="blog">
  <div class="abs label center" style="top:2493px;justify-content:center">Latest News and Updates <i></i></div>
  <h2 class="abs h2 center" style="top:2537px">Current News &amp; Blog Posts</h2>
  <p class="abs sub center" style="top:2597px">Tarrow Cat Hotel will integrate modern technology to enhance convenience and<br>provide peace of mind for pet owners.</p>

  <article class="post" style="left:161px;top:2678px">
    <div class="img" style="background:linear-gradient(135deg,#e9e4dd,#c79a74 50%,#7d5a44)" role="img" aria-label="Woman cuddling a calico cat"></div>
    <div class="meta">By <b>Tarrow Cat Hotel</b>&nbsp;&nbsp;&nbsp;&nbsp;&nbsp; 25 Febuary, 2025</div>
    <h4>The pet care industry in New Zealand has seen significant growth</h4>
    <p>driven by a high rate of pet ownership and an increasing focus on pet well-being. Approximately 64% of New Zealand households have at least one pet, with cats being particularly popular; around 41% of households have at least one cat, totaling approximately 1.2 million domestic cats. (petcensus.example)</p>
    <div class="more">Read more</div>
  </article>

  <article class="post" style="left:621px;top:2678px">
    <div class="img" style="background:linear-gradient(135deg,#d9dde2,#e2b78a 50%,#b9b0a6)" role="img" aria-label="Woman lying on the floor greeting an orange cat"></div>
    <div class="meta">By <b>Tarrow Cat Hotel</b>&nbsp;&nbsp;&nbsp;&nbsp;&nbsp; 25 Febuary, 2025</div>
    <h4>The pet care industry in New Zealand has seen significant growth</h4>
    <p>driven by a high rate of pet ownership and an increasing focus on pet well-being. Approximately 64% of New Zealand households have at least one pet, with cats being particularly popular; around 41% of households have at least one cat, totaling approximately 1.2 million domestic cats. (petcensus.example)</p>
    <div class="more">Read more</div>
  </article>
</section>

<section class="contact">
  <div class="photo-circle" style="left:82px;top:3351px;width:536px;height:536px;border:6px solid var(--purple);background:linear-gradient(135deg,#2a2a2a,#6d6d6d 45%,#c9a3d6 80%,#e3d7ea)" role="img" aria-label="Black and white cat resting on a pink blanket"></div>
  <div class="photo-circle" style="left:296px;top:3595px;width:316px;height:316px;border:6px solid var(--pink);background:linear-gradient(135deg,#e6e6e6,#8e8a86 50%,#cfd8de)" role="img" aria-label="Kitten playing with a toy on a cat tree"></div>
  <div class="abs label" style="left:659px;top:3400px">Contact us <i></i></div>
  <h2 class="abs" style="left:659px;top:3428px;font-size:46px;font-weight:700;color:var(--ink);line-height:58px">Get in touch</h2>
  <p class="abs sub" style="left:659px;top:3500px;width:370px">Tarrow Cat Hotel is a boutique boarding facility in Kaiwaro, New Zealand, designed to give cats a safe, comfortable, and stress-free stay.</p>
  <div class="field" style="top:3591px;height:42px">Name *</div>
  <div class="field" style="top:3643px;height:42px">Email *</div>
  <div class="field" style="top:3695px;height:43px">Phone *</div>
  <div class="field" style="top:3747px;height:82px">Message</div>
  <span class="abs btn" style="left:664px;top:3842px;width:112px;height:41px;line-height:41px;font-size:14px">Submit</span>
</section>

<footer class="abs footer">© 2025 tarrowcathotel.com. All Rights Reserved</footer>

</body>
</html>
```